Business Card Design for a Technology Development Company

******* PLEASE NOTE (ALL DESIGNERS): I am going to finish the competition on Monday the 9th July (NOT SATURDAY 15TH). I have some designs I like and need to get them printed next week. Please submit any designs today or tomorrow. *******

PLEASE READ ALL OF THE REQUIREMENTS!!! I've rejected lot's of designs in the past because they didn't read the basic requirements - thanks and good luck!

Quill Harbor is a UK technology / small holding company that invests in startups and develops new ideas. In addition it provides IT Professional Services.

Ideally the design will be simple, professional, smart, and sophisticated, and overall be nice to look at. You can be creative as you like with the design, equally as simple as you like - you guys are the professionals so I'll leave it to your inspiration (make sure you incorporate the logo)!
Updates

PLEASE NOTE (ALL DESIGNERS): I am going to finish the competition on Monday the 9th July (NOT SATURDAY 15TH).  I have some designs I like and need to get them printed next week.  Please submit any designs today or tomorrow.

Target Market(s)

Enterprises / corporations / public sector / technical engineers / investors. More www.brontavex.com / www.pelmora.com than www.flinkaro.com!

Industry/Entity Type

Business

Requirements
Must have
• It should be modern and any artwork (if used) should be simple
- Pastel colours, dark and light colours, and shades are preferred over bright colours
- The design should incorporate the attached Quill Harbor logo and the logo colour scheme
- The logo should be on both sides. The back should just have the logo, maybe with some additional graphics
- It must have the following information on:

FirstName SecondName
Company Position
Email: name@quillharbor.co.uk
Mobile: +44 (0) 7700 900482

- The final design should be for a UK business card, dimensions: 85mm × 55mm
- The final design should have bleed marks to allow for printing and should be given in vector formats (EPS and AI)
Nice to have
• The Logo can be separated from the font in the logo on the front of the card. This isn't necessary or required, just to know it's not a limitation.
Should not have
• No bright colours (I prefer pastel colours, dark and light colours, and shades)
- Fonts that are to thin
- Effects or designs that make it difficult to print
- Italic or old fashioned looking fonts, i.e. anything like Times New Roman is a NO!

```html
<!DOCTYPE html>
<html lang="en">
<head>
<meta charset="utf-8">
<title>Quill Harbor — Business Card</title>
<link rel="stylesheet" href="https://fonts.googleapis.com/css2?family=Questrial&display=swap">
<style>
  :root {
    --teal-deep: #17c9a0;
    --teal-mid: #3fdcb5;
    --mint-light: #8af7d9;
    --logo-teal: #1ec7a1;
    --paper: #ffffff;
    --ink-light: #ffffff;
  }
  * { margin: 0; padding: 0; box-sizing: border-box; }
  html, body {
    width: 1200px;
    height: 416px;
    overflow: hidden;
    background: var(--paper);
    font-family: "Questrial", "Century Gothic", sans-serif;
  }
  .canvas {
    position: relative;
    width: 1200px;
    height: 416px;
    background: var(--paper);
  }

  /* Front of card */
  .card-front {
    position: absolute;
    left: 0;
    top: 0;
    width: 572px;
    height: 416px;
    overflow: hidden;
    background: linear-gradient(160deg, var(--teal-deep) 0%, var(--teal-mid) 45%, var(--mint-light) 100%);
  }
  .card-front .glow {
    position: absolute;
    right: -70px;
    top: 20px;
    width: 400px;
    height: 400px;
    border-radius: 50%;
    background: radial-gradient(circle, rgba(255,255,255,0.16) 0%, rgba(255,255,255,0) 70%);
  }
  .front-brand {
    position: absolute;
    left: 52px;
    top: 180px;
    display: flex;
    align-items: center;
    gap: 9px;
    color: var(--ink-light);
  }
  .front-brand .brand-dot {
    width: 14px;
    height: 14px;
    border-radius: 50%;
    background: var(--ink-light);
  }
  .front-brand .brand-name {
    font-size: 26px;
    letter-spacing: 0.2px;
  }
  .divider {
    position: absolute;
    left: 290px;
    top: 140px;
    width: 2px;
    height: 96px;
    background: var(--ink-light);
  }
  .contact {
    position: absolute;
    left: 302px;
    top: 142px;
    color: var(--ink-light);
    font-size: 15.5px;
    line-height: 23.5px;
    list-style: none;
  }

  /* Back of card */
  .card-back {
    position: absolute;
    left: 572px;
    top: 0;
    width: 628px;
    height: 416px;
    background: var(--paper);
  }
  .back-brand {
    position: absolute;
    left: 0;
    right: 0;
    top: 168px;
    display: flex;
    justify-content: center;
    align-items: center;
    gap: 16px;
    color: var(--logo-teal);
  }
  .back-brand .brand-dot {
    width: 30px;
    height: 30px;
    border-radius: 50%;
    background: var(--logo-teal);
  }
  .back-brand .brand-name {
    font-size: 52px;
    letter-spacing: 0.3px;
  }
</style>
</head>
<body>
<main class="canvas">
  <section class="card-front" aria-label="Front of business card">
    <div class="glow"></div>
    <div class="front-brand">
      <span class="brand-dot"></span>
      <span class="brand-name">Quill Harbor</span>
    </div>
    <div class="divider"></div>
    <ul class="contact">
      <li>FirstName SecondName</li>
      <li>Company Position</li>
      <li>Email: name@quillharbor.co.uk</li>
      <li>Mobile: +44 (0) 7700 900482</li>
    </ul>
  </section>

  <section class="card-back" aria-label="Back of business card">
    <div class="back-brand">
      <span class="brand-dot"></span>
      <span class="brand-name">Quill Harbor</span>
    </div>
  </section>
</main>
</body>
</html>
```